Powerpoint template & style design project

KMaldrey Consulting is an IT technology firm specializing in mobility and telecommunications applications. We provide technical consulting to global companies that want to build mobile applications and take critical business applications and move them into the cloud.
We would like to see designs that use the color blue. The final design should communicate confidence, agility and speak to technology focused customers. Forward progress and/or motion should be conveyed.

Target Market(s)

Government customers and large enterprise companies

Industry/Entity Type

Telecommunications

Font styles to use
Sans Serif

Colors
0555a3

Requirements
Must have
• different slides: Cover page, title slide, main content, transition slide, close out slide..

```html
<!DOCTYPE html>
<html lang="en">
<head>
<meta charset="utf-8">
<title>KMaldrey Consulting – Presentation Template</title>
<link href="https://fonts.googleapis.com/css2?family=Open+Sans:wght@400;600;700&family=Roboto+Condensed:wght@400;700&display=swap" rel="stylesheet">
<style>
:root{
  --blue:#0a4c9c;
  --blue-dark:#0b3d7a;
  --blue-mid:#1f6cc4;
  --blue-light:#6ea8e3;
  --ink:#7a7a7a;
  --grey-dark:#555a60;
  --grey:#6a6a6a;
  --grey-light:#bdbdbd;
  --paper:#f1f1f2;
  --band:#d9d9d9;
  --footer:#3a3a3a;
  --canvas:#000;
  --white:#fff;
}
*{box-sizing:border-box;margin:0;padding:0}
html,body{width:1200px;height:913px;overflow:hidden;background:var(--canvas)}
body{position:relative;font-family:"Open Sans",sans-serif}
.slide{position:absolute;width:390px;height:293px;background:var(--paper);overflow:hidden}
.c1{left:7px}.c2{left:404px}.c3{left:801px}
.r1{top:4px}.r2{top:305px}.r3{top:606px}

/* cover */
.cover{background:var(--white)}
.cover .photo{position:absolute;left:0;top:0;width:390px;height:171px;border-bottom:2px solid var(--blue)}
.photo-team{background:linear-gradient(120deg,#eef3f8 0%,#c9d6e4 45%,#7f93ab 75%,#dfe7ef 100%)}
.photo-deal{background:linear-gradient(110deg,#5d7893 0%,#a9bccd 40%,#d8e1ea 60%,#41566d 100%)}
.brand{position:absolute;text-align:center;color:var(--blue)}
.brand .name{font-family:"Open Sans",sans-serif;font-weight:700;font-size:15px;letter-spacing:-.3px;white-space:nowrap}
.brand .tag{font-size:5.6px;letter-spacing:1.2px;color:#3a4a5c;font-weight:600;margin-top:1px}
.brand .dot{display:block;width:18px;height:18px;background:var(--blue);margin:0 auto 5px}
.cover .brand{left:210px;top:205px;width:170px}
.footer{position:absolute;left:0;bottom:0;width:100%;height:16px;background:var(--footer);color:var(--white);font-size:5.5px;display:flex;justify-content:space-between;align-items:center;padding:0 5px}

/* content slides */
.header{position:absolute;left:0;top:0;width:100%;height:30px;background:var(--blue);color:var(--white);display:flex;justify-content:space-between;align-items:center;padding:0 9px}
.header h1{font-family:"Roboto Condensed",sans-serif;font-weight:400;font-size:17.5px}
.header .mark{font-weight:700;font-size:7px;letter-spacing:.2px}
.baseband{position:absolute;left:0;bottom:0;width:100%;height:12px;background:var(--band)}
.h{position:absolute;font-size:7px;font-weight:700;color:var(--blue)}
.p{position:absolute;font-size:5.4px;line-height:9.6px;color:var(--ink)}

/* timeline */
.tl-line{position:absolute;left:69px;top:122px;width:246px;height:1.5px;background:var(--blue-dark)}
.year{position:absolute;top:108px;width:29px;height:29px;border-radius:50%;border:2.5px solid #c9c9c9;color:var(--white);font-size:8.5px;font-weight:700;display:flex;align-items:center;justify-content:center}
.card{position:absolute;top:143px;width:109px;height:129px;border:1px solid var(--blue);background:var(--paper)}
.card .cap{height:19px;color:var(--white);font-size:6.5px;font-weight:700;display:flex;align-items:center;justify-content:center}
.card .p{position:static;padding:6px 12px;line-height:9.7px}

/* image placeholders */
.imgbox{position:absolute;left:221px;width:149px;height:88px;background:#dcdcdc;color:#b5b5b5;font-size:6.5px;display:flex;align-items:center;justify-content:center}

svg text{font-family:"Open Sans",sans-serif}
.dh{position:absolute;font-size:7px;font-weight:600;color:#444}
.ds{position:absolute;font-size:5.4px;line-height:8.8px;color:#666}

/* close */
.close{background:var(--blue)}
.close .brand{left:20px;top:130px;width:170px;color:var(--white)}
.close .brand .tag{color:#dbe6f5}
.close .brand .dot{background:var(--white)}
.thanks{position:absolute;left:210px;top:92px;font-family:"Roboto Condensed",sans-serif;font-size:17px;color:var(--white)}
.contact{position:absolute;left:209px;top:116px;width:181px;height:106px;background:var(--white);padding:9px 11px;color:#333}
.contact .intro{font-size:9px;line-height:12px}
.contact ul{list-style:none;margin-top:9px;font-size:9px;line-height:12.5px}
.contact li{display:flex;align-items:center;gap:5px}
.contact svg{width:8px;height:8px}
</style>
</head>
<body>

<!-- cover A -->
<section class="slide cover c1 r1">
  <div class="photo photo-team" role="img" aria-label="Photo of a business team working together at a laptop in a bright office"></div>
  <div class="brand"><span class="dot"></span><div class="name">KMaldrey Consulting</div><div class="tag">MOBILE &amp; CLOUD SOLUTIONS</div></div>
  <div class="footer"><span>Copyright text here</span><span>Page : 01</span></div>
</section>

<!-- cover B -->
<section class="slide cover c2 r1">
  <div class="photo photo-deal" role="img" aria-label="Photo of two business people shaking hands, one holding a tablet"></div>
  <div class="brand"><span class="dot"></span><div class="name">KMaldrey Consulting</div><div class="tag">MOBILE &amp; CLOUD SOLUTIONS</div></div>
  <div class="footer"><span>Copyright text here</span><span>Page : 01</span></div>
</section>

<!-- timeline -->
<section class="slide c3 r1">
  <header class="header"><h1>Project Title Here</h1><span class="mark">KMaldrey Consulting</span></header>
  <div class="h" style="left:14px;top:48px">Lorem ipsum dolor sit Lorem ipsum dolor sit&nbsp; Lorem ipsum dolor sit</div>
  <p class="p" style="left:14px;top:64px;width:365px">Lorem ipsum dolor sit Lorem ipsum dolor sit Lorem ipsum dolor sit Lorem ipsum dolor sit Lorem ipsum dolor sit Lorem ipsum dolor sit Lorem ipsum dolor sit Lorem ipsum dolor sit Lorem ipsum dolor sit Lorem ipsum dolor sit Lorem ipsum dolor sit Lorem ipsum dolor sit Lorem ipsum dolor sit Lorem ipsum dolor sit</p>
  <div class="tl-line"></div>
  <div class="year" style="left:55px;background:var(--blue)">1995</div>
  <div class="year" style="left:177px;background:var(--blue-dark)">2005</div>
  <div class="year" style="left:301px;background:var(--grey)">2015</div>
  <div class="card" style="left:16px"><div class="cap" style="background:var(--blue)">TITLE HERE</div><p class="p">Lorem ipsum dolor sit Lorem ipsum dolor sit Lorem ipsum dolor sit Lorem ipsum dolor sit Lorem ipsum dolor sit Lorem ipsum dolor sit Lorem ipsum dolor sit Lorem ipsum dolor sit Lorem ipsum dolor sit Lorem ipsum dolor sit</p></div>
  <div class="card" style="left:138px;border-color:var(--blue-dark)"><div class="cap" style="background:var(--blue-dark)">TITLE HERE</div><p class="p">Lorem ipsum dolor sit Lorem ipsum dolor sit Lorem ipsum dolor sit Lorem ipsum dolor sit Lorem ipsum dolor sit Lorem ipsum dolor sit Lorem ipsum dolor sit Lorem ipsum dolor sit Lorem ipsum dolor sit Lorem ipsum dolor sit</p></div>
  <div class="card" style="left:262px;border-color:var(--grey)"><div class="cap" style="background:var(--grey)">TITLE HERE</div><p class="p">Lorem ipsum dolor sit Lorem ipsum dolor sit Lorem ipsum dolor sit Lorem ipsum dolor sit Lorem ipsum dolor sit Lorem ipsum dolor sit Lorem ipsum dolor sit Lorem ipsum dolor sit Lorem ipsum dolor sit Lorem ipsum dolor sit</p></div>
  <div class="baseband"></div>
</section>

<!-- two columns -->
<section class="slide c1 r2">
  <header class="header"><h1>Project Title Here</h1><span class="mark">KMaldrey Consulting</span></header>
  <div class="h" style="left:14px;top:62px">Lorem ipsum dolor sit Lorem ipsum dolor</div>
  <div class="h" style="left:202px;top:62px">Lorem ipsum dolor sit Lorem ipsum dolor</div>
  <p class="p" style="left:14px;top:80px;width:176px">Lorem ipsum dolor sit Lorem ipsum dolor sit Lorem ipsum dolor sit Lorem ipsum dolor sit Lorem ipsum dolor sit Lorem ipsum dolor sit Lorem ipsum dolor sit Lorem ipsum dolor sit Lorem ipsum dolor sit Lorem ipsum dolor sit Lorem ipsum dolor sit Lorem ipsum dolor sit Lorem ipsum dolor sit Lorem ipsum dolor sit</p>
  <p class="p" style="left:14px;top:160px;width:176px">Lorem ipsum dolor sit Lorem ipsum dolor sit Lorem ipsum dolor sit Lorem ipsum dolor sit Lorem ipsum dolor sit Lorem ipsum dolor sit Lorem ipsum dolor sit Lorem ipsum dolor sit Lorem ipsum dolor sit</p>
  <p class="p" style="left:14px;top:231px;width:176px">Lorem ipsum dolor sit Lorem ipsum dolor sit Lorem ipsum dolor sit Lorem ipsum dolor sit Lorem ipsum dolor sit Lorem ipsum dolor sit Lorem ipsum dolor sit</p>
  <p class="p" style="left:202px;top:80px;width:176px">Lorem ipsum dolor sit Lorem ipsum dolor sit Lorem ipsum dolor sit Lorem ipsum dolor sit Lorem ipsum dolor sit Lorem ipsum dolor sit Lorem ipsum dolor sit Lorem ipsum dolor sit Lorem ipsum dolor sit Lorem ipsum dolor sit Lorem ipsum dolor sit Lorem ipsum dolor sit Lorem ipsum dolor sit Lorem ipsum dolor sit</p>
  <p class="p" style="left:202px;top:160px;width:176px">Lorem ipsum dolor sit Lorem ipsum dolor sit Lorem ipsum dolor sit Lorem ipsum dolor sit Lorem ipsum dolor sit Lorem ipsum dolor sit Lorem ipsum dolor sit Lorem ipsum dolor sit Lorem ipsum dolor sit</p>
  <p class="p" style="left:202px;top:231px;width:176px">Lorem ipsum dolor sit Lorem ipsum dolor sit Lorem ipsum dolor sit Lorem ipsum dolor sit Lorem ipsum dolor sit Lorem ipsum dolor sit Lorem ipsum dolor sit</p>
  <div class="baseband"></div>
</section>

<!-- text with images -->
<section class="slide c2 r2">
  <header class="header"><h1>Project Title Here</h1><span class="mark">KMaldrey Consulting</span></header>
  <div class="h" style="left:14px;top:62px">Lorem ipsum dolor sit Lorem ipsum dolor</div>
  <p class="p" style="left:14px;top:80px;width:176px">Lorem ipsum dolor sit Lorem ipsum dolor sit Lorem ipsum dolor sit Lorem ipsum dolor sit Lorem ipsum dolor sit Lorem ipsum dolor sit Lorem ipsum dolor sit Lorem ipsum dolor sit Lorem ipsum dolor sit Lorem ipsum dolor sit Lorem ipsum dolor sit Lorem ipsum dolor sit Lorem ipsum dolor sit Lorem ipsum dolor sit</p>
  <p class="p" style="left:14px;top:160px;width:176px">Lorem ipsum dolor sit Lorem ipsum dolor sit Lorem ipsum dolor sit Lorem ipsum dolor sit Lorem ipsum dolor sit Lorem ipsum dolor sit Lorem ipsum dolor sit Lorem ipsum dolor sit Lorem ipsum dolor sit</p>
  <p class="p" style="left:14px;top:231px;width:176px">Lorem ipsum dolor sit Lorem ipsum dolor sit Lorem ipsum dolor sit Lorem ipsum dolor sit Lorem ipsum dolor sit Lorem ipsum dolor sit Lorem ipsum dolor sit</p>
  <div class="imgbox" style="top:62px">IMAGES</div>
  <div class="imgbox" style="top:165px">IMAGES</div>
  <div class="baseband"></div>
</section>

<!-- pie chart -->
<section class="slide c3 r2">
  <header class="header"><h1>Project Title Here</h1><span class="mark">KMaldrey Consulting</span></header>
  <div class="h" style="left:14px;top:62px">Lorem ipsum dolor sit Lorem ipsum dolor</div>
  <p class="p" style="left:14px;top:80px;width:176px">Lorem ipsum dolor sit Lorem ipsum dolor sit Lorem ipsum dolor sit Lorem ipsum dolor sit Lorem ipsum dolor sit Lorem ipsum dolor sit Lorem ipsum dolor sit Lorem ipsum dolor sit Lorem ipsum dolor sit Lorem ipsum dolor sit Lorem ipsum dolor sit Lorem ipsum dolor sit Lorem ipsum dolor sit Lorem ipsum dolor sit</p>
  <p class="p" style="left:14px;top:160px;width:176px">Lorem ipsum dolor sit Lorem ipsum dolor sit Lorem ipsum dolor sit Lorem ipsum dolor sit Lorem ipsum dolor sit Lorem ipsum dolor sit Lorem ipsum dolor sit Lorem ipsum dolor sit Lorem ipsum dolor sit</p>
  <p class="p" style="left:14px;top:231px;width:176px">Lorem ipsum dolor sit Lorem ipsum dolor sit Lorem ipsum dolor sit Lorem ipsum dolor sit Lorem ipsum dolor sit Lorem ipsum dolor sit Lorem ipsum dolor sit</p>
  <svg style="position:absolute;left:208px;top:75px" width="160" height="160" viewBox="-80 -80 160 160" aria-label="Pie chart with five segments">
    <g stroke="#f1f1f2" stroke-width="1">
      <path d="M0 0L-25.7 -70.5A75 75 0 0 1 31.7 -68Z" fill="#b9b9b9"/>
      <path d="M0 0L31.7 -68A75 75 0 0 1 70.5 25.7Z" fill="#1f6cc4"/>
      <path d="M0 0L70.5 25.7A75 75 0 0 1 25.7 70.5Z" fill="#6ea8e3"/>
      <path d="M0 0L25.7 70.5A75 75 0 0 1 -70.5 25.7Z" fill="#0b3d8a"/>
      <path d="M0 0L-70.5 25.7A75 75 0 0 1 -25.7 -70.5Z" fill="#555a60"/>
    </g>
    <circle r="11" fill="#fff" stroke="#0a4c9c" stroke-width="2"/>
    <g fill="#fff" font-size="5.2" font-weight="600" text-anchor="middle">
      <text x="-32" y="-46">Lorem</text><text x="-32" y="-40">ipsum</text><text x="-32" y="-34">dolor</text>
      <text x="3" y="-55" fill="#333">Lorem</text><text x="3" y="-49" fill="#333">ipsum</text><text x="3" y="-43" fill="#333">dolor</text>
      <text x="44" y="-18">Lorem ipsum</text><text x="44" y="-11">dolor</text>
      <text x="36" y="33" fill="#123">Lorem ipsum</text><text x="36" y="40" fill="#123">dolor</text>
      <text x="-19" y="40">Lorem ipsum dolor</text><text x="-19" y="47">Lorem ipsum dolor</text>
      <text x="-45" y="-6">Lorem ipsum dolor</text><text x="-45" y="1">Lorem ipsum dolor</text>
    </g>
  </svg>
  <div class="baseband"></div>
</section>

<!-- full-width text -->
<section class="slide c1 r3">
  <header class="header"><h1>Project Title Here</h1><span class="mark">KMaldrey Consulting</span></header>
  <div class="h" style="left:14px;top:50px">Lorem ipsum dolor sit Lorem ipsum dolor sit&nbsp; Lorem ipsum dolor sit</div>
  <p class="p" style="left:14px;top:66px;width:362px">Lorem ipsum dolor sit Lorem ipsum dolor sit Lorem ipsum dolor sit Lorem ipsum dolor sit Lorem ipsum dolor sit Lorem ipsum dolor sit Lorem ipsum dolor sit Lorem ipsum dolor sit Lorem ipsum dolor sit Lorem ipsum dolor sit Lorem ipsum dolor sit Lorem ipsum dolor sit Lorem ipsum dolor sit Lorem ipsum dolor sit</p>
  <p class="p" style="left:14px;top:110px;width:362px">Lorem ipsum dolor sit Lorem ipsum dolor sit Lorem ipsum dolor sit Lorem ipsum dolor sit Lorem ipsum dolor sit Lorem ipsum dolor sit Lorem ipsum dolor sit Lorem ipsum dolor sit Lorem ipsum dolor sit Lorem ipsum dolor sit Lorem ipsum dolor sit Lorem ipsum dolor sit Lorem ipsum dolor sit Lorem ipsum dolor sit</p>
  <p class="p" style="left:14px;top:155px;width:362px">Lorem ipsum dolor sit Lorem ipsum dolor sit Lorem ipsum dolor sit Lorem ipsum dolor sit Lorem ipsum dolor sit Lorem ipsum dolor sit Lorem ipsum dolor sit Lorem ipsum dolor sit Lorem ipsum dolor sit Lorem ipsum dolor sit Lorem ipsum dolor sit Lorem ipsum dolor sit Lorem ipsum dolor sit Lorem ipsum dolor sit</p>
  <p class="p" style="left:14px;top:209px;width:362px">Lorem ipsum dolor sit Lorem ipsum dolor sit Lorem ipsum dolor sit Lorem ipsum dolor sit Lorem ipsum dolor sit Lorem ipsum dolor sit Lorem ipsum dolor sit Lorem ipsum dolor sit Lorem ipsum dolor sit Lorem ipsum dolor sit Lorem ipsum dolor sit Lorem ipsum dolor sit Lorem ipsum dolor sit Lorem ipsum dolor sit</p>
  <div class="baseband"></div>
</section>

<!-- cycle diagram -->
<section class="slide c2 r3">
  <header class="header"><h1>Project Title Here</h1><span class="mark">KMaldrey Consulting</span></header>
  <svg style="position:absolute;left:0;top:0" width="390" height="293" viewBox="0 0 390 293" aria-label="Cycle diagram with eight segments and six headings">
    <g fill="none" stroke-width="11" transform="translate(199 140)">
      <circle r="75" stroke="#0b3d7a" stroke-dasharray="53 418" transform="rotate(-88)"/>
      <circle r="75" stroke="#0a4c9c" stroke-dasharray="53 418" transform="rotate(-43)"/>
      <circle r="75" stroke="#1b57a8" stroke-dasharray="53 418" transform="rotate(2)"/>
      <circle r="75" stroke="#8fa2a6" stroke-dasharray="53 418" transform="rotate(47)"/>
      <circle r="75" stroke="#3a3a3a" stroke-dasharray="53 418" transform="rotate(92)"/>
      <circle r="75" stroke="#4a4c5e" stroke-dasharray="53 418" transform="rotate(137)"/>
      <circle r="75" stroke="#5a5c60" stroke-dasharray="53 418" transform="rotate(182)"/>
      <circle r="75" stroke="#2d3b8c" stroke-dasharray="53 418" transform="rotate(227)"/>
    </g>
    <g fill="none" stroke-width=".8">
      <polyline points="82,73 130,73 146,86" stroke="#2d3b8c"/>
      <polyline points="82,159 130,159 142,150" stroke="#5a5c60"/>
      <polyline points="122,230 140,230 158,214" stroke="#4a4c5e"/>
      <polyline points="312,54 274,54 258,70" stroke="#0a4c9c"/>
      <polyline points="318,134 280,134 268,128" stroke="#1b57a8"/>
      <polyline points="312,219 272,219 260,203" stroke="#8fa2a6"/>
    </g>
    <text x="199" y="143" text-anchor="middle" font-size="8" font-weight="700" fill="#0a4c9c">KMaldrey</text>
  </svg>
  <div class="dh" style="left:24px;top:65px">Heading Here</div>
  <p class="ds" style="left:24px;top:75px;width:82px">Subtext here Subtext here Subtext here Subtext here Subtext here</p>
  <div class="dh" style="left:24px;top:151px">Heading Here</div>
  <p class="ds" style="left:24px;top:161px;width:82px">Subtext here Subtext here Subtext here Subtext here Subtext here</p>
  <div class="dh" style="left:24px;top:227px">Heading Here</div>
  <p class="ds" style="left:24px;top:237px;width:62px">Subtext here Subtext here Subtext here Subtext here Subtext here</p>
  <div class="dh" style="right:20px;top:53px">Heading Here</div>
  <p class="ds" style="right:20px;top:63px;width:84px;text-align:right">Subtext here Subtext here Subtext here Subtext here Subtext here</p>
  <div class="dh" style="right:15px;top:132px">Heading Here</div>
  <p class="ds" style="right:15px;top:142px;width:84px;text-align:right">Subtext here Subtext here Subtext here Subtext here Subtext here</p>
  <div class="dh" style="right:20px;top:217px">Heading Here</div>
  <p class="ds" style="right:20px;top:227px;width:84px;text-align:right">Subtext here Subtext here Subtext here Subtext here Subtext here</p>
  <div class="baseband"></div>
</section>

<!-- close -->
<section class="slide close c3 r3">
  <div class="brand"><span class="dot"></span><div class="name">KMaldrey Consulting</div><div class="tag">MOBILE &amp; CLOUD SOLUTIONS</div></div>
  <div class="thanks">Thanks for your Time</div>
  <div class="contact">
    <p class="intro">Lorem ipsum dolor sit amet,<br>consectetur adipiscing elit.<br>Donec accumsan.</p>
    <ul>
      <li><svg viewBox="0 0 10 10"><path d="M2 1l2 2-1 1.5c.7 1.3 1.5 2.1 2.5 2.5L7 6l2 2-1.5 1.5C5 9 1 5 .5 2z" fill="#333"/></svg>: 555 0142 8830</li>
      <li><svg viewBox="0 0 10 10"><rect x=".5" y="2" width="9" height="6" fill="#333"/><path d="M.5 2l4.5 3.5L9.5 2" stroke="#fff" fill="none" stroke-width=".8"/></svg>: abcde@mailnet.com</li>
      <li><svg viewBox="0 0 10 10"><path d="M9.5.5L.5 4.5l4 1 1 4z" fill="#333"/></svg>: abcdemailnet.com</li>
    </ul>
  </div>
</section>

</body>
</html>
```